PowerPoint Corporate Template for Healthcare AI Technology Company

Take logo and create a comprehensive source file for corporate PowerPoint presentation library that provides an array of title/separator slides, graphic presentation options, chart options and text slide options. Utilize the current logo files and provide options on white backgrounds, and knock out options.

Target Market(s)

Pharmaceutical Manufacturers

Font styles to use
Sans Serif

Colors
6b449b
0556a4
33a6d7
0393ce
ffffff
e34197

Requirements
Must have
• Use logos upgraded in files; create an embedded color palette that aligns to the logo; include multiple options for different types of slides including charts; create a bullet point that is the logo in the purple/blue color with white background; incorporate knock out logo version option for separator pages; must include page numbers; use font aligned to logo for text slide options
Nice to have
• Tech looking, data intensive slide options that communicate easily; could be using 3-4 data points per slide
Should not have
• Any logo other than what has been shared

```html
<!DOCTYPE html>
<html lang="en">
<head>
<meta charset="utf-8">
<title>Veridia Presentation Template Guideline</title>
<link href="https://fonts.googleapis.com/css2?family=Raleway:wght@300;400;500;600;700;800&display=swap" rel="stylesheet">
<style>
:root{
  --purple:#6b449b;
  --purple-dark:#5d3a8c;
  --blue:#0556a4;
  --sky:#33a6d7;
  --lilac:#e6dcf1;
  --lilac-soft:#efe9f6;
  --ice:#dfe9f5;
  --band:#efeff2;
  --ink:#3b3a45;
  --muted:#7d7c88;
  --white:#ffffff;
}
*{box-sizing:border-box;margin:0;padding:0}
html,body{width:1200px;height:675px;overflow:hidden;background:var(--white)}
body{position:relative;font-family:'Raleway',sans-serif;color:var(--ink)}
.slide{position:absolute;width:244px;height:137px;background:var(--white);box-shadow:0 3px 12px rgba(60,50,90,.12);overflow:hidden}
.slide > *{position:absolute}
.bar{left:12px;top:0;width:26px;height:3px;background:var(--purple)}
.ttl{left:12px;top:12px;font-size:9.5px;font-weight:400;color:#2d2c35;white-space:nowrap}
.ttl b{color:var(--purple);font-weight:700}
.band{left:0;top:28px;width:244px;height:96px;background:var(--band)}
.foot{left:12px;top:128px;font-size:4.5px;color:var(--purple);display:flex;align-items:center;gap:2px}
.foot i{display:block;width:5px;height:5px;border:.6px solid var(--purple);border-radius:50%}
.pg{right:12px;top:128px;font-size:3.5px;color:var(--muted)}
.tiny{font-size:3px;line-height:1.35;color:var(--muted)}
.tiny.w{color:rgba(255,255,255,.85)}
.photo{background:linear-gradient(120deg,#7a55b0 0%,#9b86c6 45%,#c7bfdc 100%)}
.num{font-size:11px;font-weight:600;color:var(--purple);line-height:1}
.item{display:flex;gap:3px}
.item h5{font-size:3.6px;font-weight:700;color:var(--purple)}
.item.b .num,.item.b h5{color:var(--blue)}

.hero{left:77px;top:34px;width:523px;height:294px}
.hero .bar{left:26px;width:57px;height:6px}
.hero .photo{left:0;top:30px;width:523px;height:225px;background:linear-gradient(100deg,#6b449b 0%,#7a5aad 35%,#9d8cc4 62%,#b9a793 82%,#8d7a6c 100%)}
.hero h1{left:26px;top:114px;color:var(--white);font-size:26px;line-height:1.02;font-weight:300}
.hero h1 strong{display:block;font-weight:700}
.hero .date{left:26px;top:173px;color:var(--white);font-size:9.5px;font-weight:400}
.hero .brand{left:27px;top:262px;display:flex;align-items:center;gap:6px;font-size:15px;font-weight:300;color:var(--purple)}
.hero .brand i{display:block;width:17px;height:17px;border:1.4px solid var(--purple);border-radius:50%}

.box{padding:4px 5px;color:var(--white)}
.box h4{font-size:5px;font-weight:500;margin:3px 0 2px}
.ico{width:9px;height:9px}

.tbl{border-collapse:collapse;font-size:2.8px;color:var(--ink)}
.tbl th{color:var(--purple);font-weight:700;padding:1.5px 2px;border-bottom:.5px solid #c9c2d6;text-align:center}
.tbl td{padding:2.2px 2px;border-bottom:.3px solid #dedbe5;text-align:center}
.tbl td:first-child{text-align:left}
.tbl td:last-child{background:var(--lilac);color:var(--purple);font-weight:700}

.quote{position:absolute;width:91px;height:36px;padding:4px 6px;color:var(--white);font-size:3.4px;line-height:1.35}
.quote b{display:block;font-size:6px;line-height:.8}
.quote em{display:block;font-style:normal;font-weight:700;margin-top:1px}
.quote:after{content:"";position:absolute;right:14px;bottom:-4px;border:4px solid transparent;border-bottom:0;border-top-color:inherit}
.quote.p{background:var(--purple);border-color:var(--purple)}
.quote.u{background:var(--blue);border-color:var(--blue)}
</style>
</head>
<body>

<section class="slide hero">
  <div class="bar"></div>
  <div class="photo" role="img" aria-label="Photo of a smiling woman seated at a desk by a window, washed in purple"></div>
  <h1>Presentation<strong>Template Guideline</strong></h1>
  <div class="date">June 2020</div>
  <div class="brand"><i></i>Veridia</div>
</section>

<section class="slide" style="left:634px;top:34px">
  <div class="band" style="top:14px;height:104px"></div>
  <div class="photo" style="left:0;top:14px;width:122px;height:104px;background:linear-gradient(160deg,#8a6cc0 0%,#a899c9 45%,#7b8a6a 100%)" role="img" aria-label="Photo of a woman with open arms in a grassy field"></div>
  <div class="num" style="left:130px;top:46px;font-size:15px;font-weight:800">01</div>
  <div style="left:130px;top:62px;font-size:9.5px;color:var(--purple);font-weight:300">Section Slide</div>
  <div class="tiny" style="left:130px;top:80px;width:95px;color:var(--purple)">Short intro line for this section, kept brief and clear for readers.</div>
  <div class="foot"><i></i>Veridia</div><div class="pg">2</div>
</section>

<section class="slide" style="left:912px;top:34px">
  <div class="bar"></div>
  <div class="ttl">Table of <b>Content</b></div>
  <div class="band"></div>
  <div style="left:0;top:28px;width:181px;height:96px;background:var(--purple)"></div>
  <ul style="left:12px;top:38px;width:165px;list-style:none;color:var(--white)">
    <li style="font-size:5px;margin-bottom:5px">• Introduce<div class="tiny w" style="padding-left:5px;font-size:2.6px">Overview of the company, its mission and the goals of this deck.</div></li>
    <li style="font-size:5px;margin-bottom:5px">• Progam Development<div class="tiny w" style="padding-left:5px;font-size:2.6px">How programs are built, tested and delivered to partner teams.</div></li>
    <li style="font-size:5px;margin-bottom:5px">• Challenging<div class="tiny w" style="padding-left:5px;font-size:2.6px">Key risks, open questions and areas needing further focus.</div></li>
    <li style="font-size:5px">• Future Step<div class="tiny w" style="padding-left:5px;font-size:2.6px">Next milestones, timelines and the owners for each action.</div></li>
  </ul>
  <div class="foot"><i></i>Veridia</div><div class="pg">3</div>
</section>

<section class="slide" style="left:634px;top:190px">
  <div class="bar"></div>
  <div class="ttl">About <b>Company</b></div>
  <div class="band"></div>
  <div class="tiny" style="left:12px;top:44px;width:100px"><span style="color:var(--purple);font-weight:700">We build clinical data tools that help manufacturers move faster with fewer errors.</span> Our team blends research, engineering and care expertise.<br><br>Founded to make trial data simple, we now serve partners across many regions, with secure platforms, clear reporting and close support from start to finish of every project we run.</div>
  <div class="box" style="left:126px;top:28px;width:51px;height:96px;background:var(--purple)">
    <svg class="ico" viewBox="0 0 10 10"><path d="M1 5.5l2.5 2.5L9 2" fill="none" stroke="#fff" stroke-width="1"/></svg>
    <h4>Vision</h4>
    <div class="tiny w">A world where every treatment reaches patients sooner through smart, reliable data and shared insight across teams.</div>
  </div>
  <div class="box" style="left:181px;top:28px;width:51px;height:96px;background:var(--blue)">
    <svg class="ico" viewBox="0 0 10 10"><circle cx="5" cy="5" r="4" fill="none" stroke="#fff" stroke-width=".7"/><path d="M5 0v3M5 7v3M0 5h3M7 5h3" stroke="#fff" stroke-width=".7"/></svg>
    <h4>Mission</h4>
    <div class="tiny w">To give partners accurate, timely analysis that guides decisions, cuts waste and keeps quality at the core.</div>
  </div>
  <div class="foot"><i></i>Veridia</div><div class="pg">4</div>
</section>

<section class="slide" style="left:912px;top:190px">
  <div class="bar"></div>
  <div class="ttl">Our <b>Services</b></div>
  <div class="tiny" style="left:12px;top:30px;width:222px"><span style="color:var(--purple);font-weight:700">We offer data, analysis and advisory services built for pharmaceutical teams of every size.</span> Each service is shaped around your goals and timelines.</div>
  <div class="band" style="top:48px;height:76px"></div>
  <div class="box" style="left:22px;top:41px;width:97px;height:40px;background:var(--purple)">
    <svg class="ico" viewBox="0 0 10 10"><circle cx="5" cy="5" r="4" fill="none" stroke="#fff" stroke-width=".7"/><path d="M3 4h4M3 6h3" stroke="#fff" stroke-width=".7"/></svg>
    <h4>Communication</h4>
    <div class="tiny w">Clear reporting and regular updates that keep every team aligned.</div>
  </div>
  <div class="box" style="left:125px;top:41px;width:97px;height:40px;background:var(--blue)">
    <svg class="ico" viewBox="0 0 10 10"><rect x="1" y="2" width="8" height="7" fill="none" stroke="#fff" stroke-width=".7"/><path d="M1 4h8M3 1v2M7 1v2" stroke="#fff" stroke-width=".7"/></svg>
    <h4>Event in Years</h4>
    <div class="tiny w">A steady record of milestones delivered across many partner programs.</div>
  </div>
  <div class="item" style="left:18px;top:95px;width:50px"><span class="num">1</span><div><h5>Lorem ipsum.</h5><div class="tiny" style="font-size:2.6px">Quick note on this point here.</div></div></div>
  <div class="item" style="left:72px;top:95px;width:50px"><span class="num">2</span><div><h5>Lorem ipsum.</h5><div class="tiny" style="font-size:2.6px">Quick note on this point here.</div></div></div>
  <div class="item" style="left:126px;top:95px;width:50px"><span class="num">3</span><div><h5>Lorem ipsum.</h5><div class="tiny" style="font-size:2.6px">Quick note on this point here.</div></div></div>
  <div class="item" style="left:180px;top:95px;width:50px"><span class="num">4</span><div><h5>Lorem ipsum.</h5><div class="tiny" style="font-size:2.6px">Quick note on this point here.</div></div></div>
  <div class="foot"><i></i>Veridia</div><div class="pg">5</div>
</section>

<section class="slide" style="left:77px;top:352px">
  <div class="bar"></div>
  <div class="ttl">Service <b>Details</b></div>
  <div class="band"></div>
  <div style="left:0;top:28px;width:68px;height:96px;background:var(--purple)"></div>
  <div style="left:12px;top:50px;width:52px;font-size:4.3px;line-height:1.3;color:var(--white)">We guide each program from first data to final report, with steady checks and open talks with your team at every stage along the way.</div>
  <div class="item" style="left:80px;top:47px;width:70px"><span class="num">1</span><div style="width:58px"><h5>Lorem ipsum.</h5><div class="tiny" style="font-size:2.6px">Short detail on this step.</div><div style="height:1.2px;background:#d5d3dc;margin-top:2px"><div style="width:60%;height:100%;background:var(--blue)"></div></div></div></div>
  <div style="left:138px;top:66px;font-size:3.2px;color:var(--purple);font-weight:700">60%</div>
  <div class="item" style="left:80px;top:82px;width:70px"><span class="num">2</span><div style="width:58px"><h5>Lorem ipsum.</h5><div class="tiny" style="font-size:2.6px">Short detail on this step.</div><div style="height:1.2px;background:#d5d3dc;margin-top:2px"><div style="width:80%;height:100%;background:var(--blue)"></div></div></div></div>
  <div style="left:138px;top:101px;font-size:3.2px;color:var(--purple);font-weight:700">80%</div>
  <div style="left:165px;top:33px;width:62px;height:91px;background:linear-gradient(180deg,#d9d6de,#bfbcc8)" role="img" aria-label="Hand holding a smartphone showing capsules"></div>
  <div class="foot"><i></i>Veridia</div><div class="pg">6</div>
</section>

<section class="slide" style="left:356px;top:352px">
  <div class="bar"></div>
  <div class="ttl">Selected <b>Program</b></div>
  <div style="left:12px;top:33px;width:222px;height:74px;display:flex;gap:3px">
    <div class="box" style="flex:1;background:var(--lilac);color:var(--purple);position:relative"><h4 style="margin-top:13px">Communication</h4><div class="tiny" style="color:var(--purple)">Short summary of this program area.</div>
      <svg style="position:absolute;left:14px;top:46px" width="22" height="22" viewBox="0 0 22 22"><circle cx="11" cy="11" r="9" fill="none" stroke="#fff" stroke-width="2"/><circle cx="11" cy="11" r="9" fill="none" stroke="#c4b3de" stroke-width="2" stroke-dasharray="11.3 56.5" transform="rotate(-90 11 11)"/><text x="11" y="12.8" font-size="5" font-weight="700" text-anchor="middle" fill="#6b449b" font-family="Raleway,sans-serif">20%</text></svg></div>
    <div class="box" style="flex:1;background:var(--purple);position:relative"><h4 style="margin-top:13px">Leader</h4><div class="tiny w">Short summary of this program area.</div>
      <svg style="position:absolute;left:14px;top:46px" width="22" height="22" viewBox="0 0 22 22"><circle cx="11" cy="11" r="9" fill="none" stroke="#8c6ab8" stroke-width="2"/><circle cx="11" cy="11" r="9" fill="none" stroke="#fff" stroke-width="2" stroke-dasharray="42.4 56.5" transform="rotate(-90 11 11)"/><text x="11" y="12.8" font-size="5" font-weight="700" text-anchor="middle" fill="#fff" font-family="Raleway,sans-serif">75%</text></svg></div>
    <div class="box" style="flex:1;background:var(--lilac);color:var(--purple);position:relative"><h4 style="margin-top:13px">Global</h4><div class="tiny" style="color:var(--purple)">Short summary of this program area.</div>
      <svg style="position:absolute;left:14px;top:46px" width="22" height="22" viewBox="0 0 22 22"><circle cx="11" cy="11" r="9" fill="none" stroke="#fff" stroke-width="2"/><circle cx="11" cy="11" r="9" fill="none" stroke="#c4b3de" stroke-width="2" stroke-dasharray="28.3 56.5" transform="rotate(-90 11 11)"/><text x="11" y="12.8" font-size="5" font-weight="700" text-anchor="middle" fill="#6b449b" font-family="Raleway,sans-serif">50%</text></svg></div>
    <div class="box" style="flex:1;background:var(--lilac);color:var(--purple);position:relative"><h4 style="margin-top:13px">Recycle</h4><div class="tiny" style="color:var(--purple)">Short summary of this program area.</div>
      <svg style="position:absolute;left:14px;top:46px" width="22" height="22" viewBox="0 0 22 22"><circle cx="11" cy="11" r="9" fill="none" stroke="#fff" stroke-width="2"/><circle cx="11" cy="11" r="9" fill="none" stroke="#c4b3de" stroke-width="2" stroke-dasharray="17 56.5" transform="rotate(-90 11 11)"/><text x="11" y="12.8" font-size="5" font-weight="700" text-anchor="middle" fill="#6b449b" font-family="Raleway,sans-serif">30%</text></svg></div>
  </div>
  <div class="tiny" style="left:12px;top:110px;width:50px">Brief note under this card.</div>
  <div class="tiny" style="left:68px;top:110px;width:50px;color:var(--purple);font-weight:700">Brief note under this card.</div>
  <div class="tiny" style="left:123px;top:110px;width:50px">Brief note under this card.</div>
  <div class="tiny" style="left:179px;top:110px;width:50px">Brief note under this card.</div>
  <div class="foot"><i></i>Veridia</div><div class="pg">7</div>
</section>

<section class="slide" style="left:634px;top:352px">
  <div class="bar"></div>
  <div class="ttl">Slide <b>Tables</b></div>
  <table class="tbl" style="left:12px;top:34px;width:170px">
    <tr><th>Programs</th><th>Risk Status</th><th>Indicator A</th><th>Indicator B</th><th>Duration</th><th style="background:none">Percentages</th></tr>
    <tr><td>Oncology Care</td><td>High</td><td>Green</td><td>Green</td><td>14 Months</td><td>40%</td></tr>
    <tr><td>Cardiology</td><td>High</td><td>Green</td><td>Green</td><td>12 Months</td><td>50%</td></tr>
    <tr><td>Pharmacy Data</td><td>High</td><td>Blue</td><td>Yellow</td><td>6 Months</td><td>70%</td></tr>
    <tr><td>Bulk Testing</td><td>Medium</td><td>Yellow</td><td>Red</td><td>8 Months</td><td>70%</td></tr>
    <tr><td>Remote Care</td><td>Medium</td><td>Yellow</td><td>Yellow</td><td>24 Months</td><td>60%</td></tr>
    <tr><td>Lab Research</td><td>Medium</td><td>Green</td><td>Yellow</td><td>24 Months</td><td>10%</td></tr>
  </table>
  <div class="box" style="left:184px;top:33px;width:49px;height:66px;background:var(--purple)">
    <svg class="ico" viewBox="0 0 10 10"><circle cx="3" cy="3" r="1.5" fill="none" stroke="#fff" stroke-width=".6"/><circle cx="7" cy="3" r="1.5" fill="none" stroke="#fff" stroke-width=".6"/><path d="M1 8c0-2 4-2 4 0M5 8c0-2 4-2 4 0" fill="none" stroke="#fff" stroke-width=".6"/></svg>
    <h4 style="font-size:5.5px">Internal Team</h4>
    <div class="tiny w">A small core team leads each program with clear roles and owners.</div>
  </div>
  <div class="tiny" style="left:12px;top:105px;width:106px">Notes on the table, with a short read of the key figures and trends shown above.</div>
  <div class="tiny" style="left:126px;top:105px;width:106px">Further notes on status and timing, with next checks planned for each line.</div>
  <div class="foot"><i></i>Veridia</div><div class="pg">8</div>
</section>

<section class="slide" style="left:912px;top:352px">
  <div class="bar"></div>
  <div class="ttl">Our <b>Focus</b></div>
  <div class="band"></div>
  <div style="left:0;top:28px;width:77px;height:96px;background:var(--lilac-soft)"></div>
  <div style="left:166px;top:28px;width:78px;height:96px;background:var(--ice)"></div>
  <svg style="left:0;top:28px" width="244" height="96" viewBox="0 0 244 96">
    <path d="M87 21L104 36M87 48H100M87 75L104 60M157 21L140 36M157 48H144M157 75L140 60" stroke="#c9c5d3" stroke-width=".5" fill="none"/>
    <circle cx="122" cy="48" r="21" fill="#fff"/>
  </svg>
  <div style="left:106px;top:73px;font-size:6px;color:var(--purple);display:flex;align-items:center;gap:1.5px;font-weight:300"><span style="display:block;width:5px;height:5px;border:.6px solid var(--purple);border-radius:50%"></span>Veridia</div>
  <div style="left:10px;top:38px;width:56px;text-align:right"><h5 style="font-size:5px;color:var(--purple)">Target</h5><div class="tiny" style="font-size:2.5px">Who we serve and why it matters.</div></div>
  <div style="left:10px;top:66px;width:56px;text-align:right"><h5 style="font-size:5px;color:var(--purple)">Security</h5><div class="tiny" style="font-size:2.5px">Data kept safe at every stage.</div></div>
  <div style="left:10px;top:94px;width:56px;text-align:right"><h5 style="font-size:5px;color:var(--purple)">Employees</h5><div class="tiny" style="font-size:2.5px">Skilled people behind each result.</div></div>
  <div style="left:70px;top:41px;width:16px;height:16px;background:var(--purple)"></div>
  <div style="left:70px;top:69px;width:16px;height:16px;background:var(--purple)"></div>
  <div style="left:70px;top:97px;width:16px;height:16px;background:var(--purple)"></div>
  <div style="left:158px;top:41px;width:16px;height:16px;background:var(--blue)"></div>
  <div style="left:158px;top:69px;width:16px;height:16px;background:var(--blue)"></div>
  <div style="left:158px;top:97px;width:16px;height:16px;background:var(--blue)"></div>
  <svg style="left:70px;top:41px" width="104" height="72" viewBox="0 0 104 72" fill="none" stroke="#fff" stroke-width=".7">
    <circle cx="8" cy="8" r="4"/><path d="M8 3v2M8 11v2M3 8h2M11 8h2"/>
    <path d="M8 31l4 1.5v3c0 2.5-2 4-4 5-2-1-4-2.5-4-5v-3z"/>
    <circle cx="6" cy="62" r="1.5"/><circle cx="10" cy="62" r="1.5"/><path d="M4 67c0-2 4-2 4 0M8 67c0-2 4-2 4 0"/>
    <circle cx="95" cy="6" r="2"/><path d="M91 12c0-3 8-3 8 0z"/>
    <path d="M92 39v-3M95 39v-5M98 39v-7"/>
    <circle cx="96" cy="64" r="4"/><path d="M94 64h.5M96 64h.5M98 64h.5"/>
  </svg>
  <div style="left:178px;top:38px;width:56px"><h5 style="font-size:5px;color:var(--blue)">Acquisition</h5><div class="tiny" style="font-size:2.5px">New partners added each quarter.</div></div>
  <div style="left:178px;top:66px;width:56px"><h5 style="font-size:5px;color:var(--blue)">Growth</h5><div class="tiny" style="font-size:2.5px">Steady gains year over year.</div></div>
  <div style="left:178px;top:94px;width:56px"><h5 style="font-size:5px;color:var(--blue)">Communication</h5><div class="tiny" style="font-size:2.5px">Open updates for every team.</div></div>
  <div class="foot"><i></i>Veridia</div><div class="pg">9</div>
</section>

<section class="slide" style="left:77px;top:509px">
  <div class="bar"></div>
  <div class="ttl">Customer <b>Feedback</b></div>
  <div class="band"></div>
  <div class="quote p" style="left:27px;top:35px"><b>“</b>Clear results and a team that always listened to what we needed.<em>- Doctor</em></div>
  <div class="quote u" style="left:125px;top:35px"><b>“</b>Fast, careful work that kept our trial right on schedule.<em>- Scientist</em></div>
  <div class="quote u" style="left:27px;top:80px"><b>“</b>Their reports made complex data easy for our board to follow.<em>- Client A</em></div>
  <div class="quote p" style="left:125px;top:80px"><b>“</b>Great support from start to finish, with no surprises at all.<em>- Customer XYZ</em></div>
  <div class="foot"><i></i>Veridia</div><div class="pg">10</div>
</section>

<section class="slide" style="left:356px;top:509px">
  <div class="bar"></div>
  <div class="ttl">Performance Last <b>10 Days</b></div>
  <div class="band"></div>
  <div class="tiny" style="left:12px;top:33px;width:140px;color:var(--ink)"><b>Daily results across two regions</b> over ten days.</div>
  <div style="left:12px;top:43px;width:30px;height:10px;background:var(--blue);font-size:2px;color:#fff;padding:1px">Peak week note</div>
  <svg style="left:10px;top:36px" width="160" height="84" viewBox="0 0 160 84">
    <path d="M4 70H150" stroke="#c9c5d3" stroke-width=".4"/>
    <polyline points="7,53 21,50 36,47 51,43 66,40 81,37 96,33 111,28 125,23 140,19" fill="none" stroke="#6b449b" stroke-width=".8"/>
    <polyline points="7,70 21,66 36,64 51,62 66,61 81,59 96,58 111,55 125,53 140,50" fill="none" stroke="#0556a4" stroke-width=".8"/>
    <polyline points="7,76 21,71 36,69 51,67 66,65 81,63 96,61 111,58 125,56 140,53" fill="none" stroke="#33a6d7" stroke-width=".6"/>
    <g fill="#6b449b"><circle cx="7" cy="53" r="1"/><circle cx="36" cy="47" r="1"/><circle cx="66" cy="40" r="1"/><circle cx="96" cy="33" r="1"/><circle cx="125" cy="23" r="1"/><circle cx="140" cy="19" r="1"/></g>
    <g fill="#0556a4"><circle cx="7" cy="70" r="1"/><circle cx="36" cy="64" r="1"/><circle cx="66" cy="61" r="1"/><circle cx="96" cy="58" r="1"/><circle cx="125" cy="53" r="1"/><circle cx="140" cy="50" r="1"/></g>
    <text x="145" y="19" font-size="2.4" fill="#6b449b">REGION A</text>
    <text x="145" y="51" font-size="2.4" fill="#33a6d7">REGION B</text>
    <g font-size="2.4" fill="#7d7c88" text-anchor="middle"><text x="7" y="78">26</text><text x="21" y="78">27</text><text x="36" y="78">28</text><text x="51" y="78">29</text><text x="66" y="78">30</text><text x="81" y="78">31</text><text x="96" y="78">01</text><text x="111" y="78">02</text><text x="125" y="78">03</text><text x="140" y="78">04</text></g>
  </svg>
  <div class="item" style="left:184px;top:38px;width:52px"><span class="num">1</span><div><h5>Lorem ipsum.</h5><div class="tiny" style="font-size:2.6px">Short note on this result.</div></div></div>
  <div class="item" style="left:184px;top:64px;width:52px"><span class="num">2</span><div><h5>Lorem ipsum.</h5><div class="tiny" style="font-size:2.6px">Short note on this result.</div></div></div>
  <div class="item" style="left:184px;top:90px;width:52px"><span class="num">3</span><div><h5>Lorem ipsum.</h5><div class="tiny" style="font-size:2.6px">Short note on this result.</div></div></div>
  <div class="foot"><i></i>Veridia</div><div class="pg">11</div>
</section>

<section class="slide" style="left:634px;top:509px">
  <div class="bar"></div>
  <div class="ttl">Service <b>Locations</b></div>
  <div class="band"></div>
  <div style="left:12px;top:34px;width:78px;font-size:4.3px;line-height:1.2;color:var(--ink)"><span style="color:var(--purple);font-weight:700">We work across many regions with local teams.</span> Each site offers the same service level to all partners.</div>
  <div style="left:96px;top:34px;width:36px"><div style="font-size:3.4px;font-weight:700">Services Location</div><div class="tiny" style="font-size:2.3px">Where our teams run field and lab work.</div></div>
  <div class="item" style="left:12px;top:67px;width:52px"><span class="num">1</span><div><h5>Lorem ipsum.</h5><div class="tiny" style="font-size:2.4px">Short site note here.</div></div></div>
  <div class="item b" style="left:66px;top:67px;width:52px"><span class="num">2</span><div><h5>Lorem ipsum.</h5><div class="tiny" style="font-size:2.4px">Short site note here.</div></div></div>
  <div class="item b" style="left:12px;top:90px;width:52px"><span class="num">3</span><div><h5>Lorem ipsum.</h5><div class="tiny" style="font-size:2.4px">Short site note here.</div></div></div>
  <div class="item" style="left:66px;top:90px;width:52px"><span class="num">4</span><div><h5>Lorem ipsum.</h5><div class="tiny" style="font-size:2.4px">Short site note here.</div></div></div>
  <div style="left:132px;top:38px;width:58px;height:82px;background:linear-gradient(180deg,#cfcdd6 0%,#b7b3c6 45%,#8e73ba 100%)" role="img" aria-label="Map of service regions with two highlighted areas"></div>
  <svg style="left:170px;top:48px" width="30" height="40" viewBox="0 0 30 40"><path d="M0 4H26M0 38H26" stroke="#0556a4" stroke-width=".4"/><circle cx="26" cy="4" r=".9" fill="#0556a4"/><circle cx="26" cy="38" r=".9" fill="#0556a4"/></svg>
  <div style="left:198px;top:49px;width:40px"><h5 style="font-size:4.5px;color:var(--blue)">Area A</h5><div class="tiny" style="font-size:2.4px">Main hub for lab and data work.</div></div>
  <div style="left:198px;top:83px;width:40px"><h5 style="font-size:4.5px;color:var(--blue)">Area B</h5><div class="tiny" style="font-size:2.4px">Second hub for field studies.</div></div>
  <div class="foot"><i></i>Veridia</div><div class="pg">12</div>
</section>

<section class="slide" style="left:912px;top:509px">
  <div class="bar"></div>
  <div class="ttl">Thank <b>You</b></div>
  <div style="left:0;top:28px;width:244px;height:96px;background:var(--purple)"></div>
  <div class="tiny w" style="left:12px;top:34px;width:170px;font-size:2.8px"><b>Thank you for your time. We look forward to working together on your next program.</b> Reach out with any questions about this deck.<br><br>Our team is ready to help plan the next steps, share more data and set up a follow-up meeting soon.</div>
  <div class="foot"><i></i>Veridia</div><div class="pg">13</div>
</section>

</body>
</html>
```